KVO-Business Card Design

I need a modern, professional business card design that includes my logo as the main feature, maybe the entire background with the contact info overlaying or even contact info on the back and the logo full frontal

Neat and organized placement of contact information

Would like to see options in black and white

Target Market(s)

real estate Developers, Construction managers, business and home owners

Industry/Entity Type

Construction

Contact Information for Business Card

KVO Construction
Danny Ferrante
General Contractor

Office: 1-888-902-7315 Ext #1
Cell: 215-730-4162
Fax: 1-888-902-7315

Font styles to use
Serif

Requirements
Must have
• title
• office #
• cell #
• Email
• website
Nice to have
• fax

```html
<!DOCTYPE html>
<html lang="en">
<head>
<meta charset="utf-8">
<title>KVO Construction – Business Card</title>
<link rel="stylesheet" href="https://fonts.googleapis.com/css2?family=Lato:wght@400;700;900&display=swap">
<style>
  :root {
    --canvas: #d9d9db;
    --card-black: #111111;
    --card-white: #ffffff;
    --band-light: #4b4b4d;
    --band-dark: #2c2c2e;
    --ink: #111111;
    --paper: #ffffff;
    --brand-green: #5cbf2a;
    --shadow: rgba(0, 0, 0, 0.28);
  }
  * { box-sizing: border-box; margin: 0; padding: 0; }
  html, body {
    width: 1200px; height: 800px; overflow: hidden;
    background: var(--canvas);
    font-family: "Lato", Arial, sans-serif;
  }
  .sheet {
    width: 1200px; height: 800px;
    display: flex; align-items: center; justify-content: center; gap: 60px;
  }
  .card {
    width: 520px; height: 297px;
    box-shadow: 0 10px 24px var(--shadow);
    position: relative; overflow: hidden;
  }

  /* Contact side */
  .card--contact { display: flex; background: var(--card-black); }
  .identity {
    width: 196px; background: var(--card-white);
    display: flex; flex-direction: column; align-items: center; justify-content: center;
    gap: 10px; padding: 0 14px;
  }
  .identity__mark {
    display: flex; align-items: center; gap: 8px;
    font-weight: 900; font-size: 30px; color: var(--ink); letter-spacing: 2px;
  }
  .identity__square { width: 14px; height: 14px; background: var(--ink); }
  .pill {
    width: 100%; background: var(--ink); color: var(--paper);
    border-radius: 7px; text-align: center;
    font-size: 15px; padding: 5px 0; letter-spacing: 0.5px;
  }
  .identity__name { font-weight: 900; font-size: 18px; color: var(--ink); }
  .divider {
    width: 18px; display: flex; justify-content: space-between;
    background: var(--card-white);
  }
  .divider span { width: 6px; background: var(--ink); }
  .divider span:last-child { width: 8px; }
  .contacts {
    flex: 1; display: flex; flex-direction: column; justify-content: center; gap: 8px;
    padding: 18px 0;
  }
  .contact-row {
    height: 38px; display: flex; align-items: center;
    padding-left: 20px; color: var(--paper); font-size: 15px;
    background: linear-gradient(90deg, var(--band-light), var(--band-dark));
    border-left: 5px solid var(--card-white);
  }
  .contact-row:nth-child(even) { background: linear-gradient(90deg, var(--band-dark), var(--band-light)); }
  .contact-row b { font-weight: 700; margin-right: 5px; }

  /* Brand side */
  .card--brand {
    background: var(--card-black);
    display: flex; align-items: center; justify-content: center; gap: 16px;
  }
  .brand__name { font-weight: 900; font-size: 52px; color: var(--brand-green); letter-spacing: 1px; }
  .brand__square { width: 26px; height: 26px; background: var(--brand-green); }
</style>
</head>
<body>
  <main class="sheet">
    <section class="card card--contact" aria-label="Business card, contact side">
      <div class="identity">
        <div class="identity__mark"><span class="identity__square"></span>KVO</div>
        <div class="pill">KVO Construction</div>
        <div class="identity__name">Danny Ferrante</div>
        <div class="pill">General Contractor</div>
      </div>
      <div class="divider"><span></span><span></span></div>
      <div class="contacts">
        <div class="contact-row"><b>Site</b>: www.kvobuild.com</div>
        <div class="contact-row"><b>Email</b>: danny@kvobuild.com</div>
        <div class="contact-row"><b>Cell</b>: 215-730-4162</div>
        <div class="contact-row"><b>Office</b>: 1-888-902-7315 Ext #1</div>
        <div class="contact-row"><b>Fax</b>: 1-888-902-7315</div>
      </div>
    </section>

    <section class="card card--brand" aria-label="Business card, brand side">
      <span class="brand__square"></span>
      <span class="brand__name">KVO Construction</span>
    </section>
  </main>
</body>
</html>
```